Ashby Meadows Thank-You Tag

Looking for a file that incorporates current branding/colors and says:

"Thanks for Swimming with Us!"
Ashby Meadows Otters

Samples of other pieces we've done recently are attached.

Will be printed on cardstock that is
Width: 3.5 inches
Height: 2.5 inches

```html
<!DOCTYPE html>
<html lang="en">
<head>
<meta charset="utf-8">
<title>Ashby Meadows Thank-You Tag</title>
<link rel="stylesheet" href="https://fonts.googleapis.com/css2?family=Montserrat:wght@600;700&family=Kaushan+Script&family=Barlow+Condensed:wght@800&family=Barlow:wght@600&display=swap">
<style>
  :root {
    --stage: #d0d0d0;
    --pool-blue: #1a44a0;
    --deep-blue: #133a91;
    --ink-blue: #2a4ea0;
    --splash-pink: #f05aa0;
    --sky-blue: #8bbde6;
    --white: #ffffff;
  }
  * { margin: 0; padding: 0; box-sizing: border-box; }
  html, body {
    width: 809px; height: 1200px; overflow: hidden;
    background: var(--stage);
  }
  .tag {
    position: absolute; left: 95px; width: 619px; height: 441px;
    box-shadow: 0 6px 22px rgba(0,0,0,0.28);
    overflow: hidden;
  }
  .tag--front { top: 106px; background: var(--pool-blue); }
  .tag--back { top: 653px; background: var(--white); }
  .tag svg { display: block; width: 619px; height: 441px; }
  .year-digit { font-family: "Montserrat", sans-serif; font-weight: 700; font-size: 200px; }
  .badge-name { font-family: "Montserrat", sans-serif; font-weight: 700; font-size: 13px; fill: var(--white); letter-spacing: 0.5px; }
  .thanks { font-family: "Kaushan Script", cursive; font-size: 58px; fill: var(--ink-blue); }
  .for { font-family: "Montserrat", sans-serif; font-weight: 600; font-size: 17px; fill: var(--ink-blue); letter-spacing: 1px; }
  .swimming { font-family: "Barlow Condensed", sans-serif; font-weight: 800; font-size: 74px; fill: var(--splash-pink); }
  .with-us { font-family: "Kaushan Script", cursive; font-size: 24px; fill: var(--white); }
  .team-name { font-family: "Barlow", sans-serif; font-weight: 600; font-size: 29px; letter-spacing: 6px; }
  .splash { fill: none; stroke-linecap: round; stroke-width: 7; }
</style>
</head>
<body>

<section class="tag tag--front" aria-label="Front of tag">
  <svg viewBox="0 0 619 441" xmlns="http://www.w3.org/2000/svg">
    <!-- year -->
    <text class="year-digit" x="180" y="189" fill="var(--white)">2</text>
    <circle cx="362" cy="134" r="73" fill="var(--white)"/>
    <circle cx="362" cy="134" r="49" fill="var(--pool-blue)"/>
    <text class="badge-name" x="362" y="131" text-anchor="middle">ASHBY</text>
    <text class="badge-name" x="362" y="147" text-anchor="middle">MEADOWS</text>
    <text class="year-digit" x="224" y="311" fill="var(--white)">2</text>
    <text class="year-digit" x="308" y="354" fill="var(--splash-pink)">6</text>

    <!-- splashes -->
    <g class="splash">
      <path d="M182 224 Q210 216 230 236" stroke="var(--sky-blue)"/>
      <path d="M162 252 Q200 242 220 250" stroke="var(--splash-pink)"/>
      <path d="M172 284 Q185 262 212 262" stroke="var(--sky-blue)"/>
      <path d="M438 298 Q452 280 488 276" stroke="var(--sky-blue)"/>
      <path d="M444 306 Q480 296 510 308" stroke="var(--splash-pink)"/>
      <path d="M450 316 Q480 314 500 338" stroke="var(--sky-blue)"/>
    </g>

    <!-- waves -->
    <path d="M0 366 C70 358 140 398 220 396 C280 394 320 372 360 372 L0 441Z" fill="var(--sky-blue)"/>
    <path d="M0 404 C80 388 150 430 240 395 C300 372 360 368 420 390 C500 420 570 415 619 398 L619 441 L0 441Z" fill="var(--splash-pink)"/>
    <path d="M0 404 C80 388 150 430 240 395" fill="none" stroke="var(--deep-blue)" stroke-width="2"/>
    <path d="M390 380 C470 420 560 420 619 372 L619 396 C560 418 490 420 420 390Z" fill="var(--white)"/>
  </svg>
</section>

<section class="tag tag--back" aria-label="Back of tag">
  <svg viewBox="0 0 619 441" xmlns="http://www.w3.org/2000/svg">
    <defs>
      <linearGradient id="illustration-tone" x1="0" y1="0" x2="1" y2="1">
        <stop offset="0" stop-color="#dbe6f6"/>
        <stop offset="1" stop-color="#f6dbe9"/>
      </linearGradient>
    </defs>

    <rect x="54" y="32" width="240" height="213" rx="14" fill="url(#illustration-tone)"
          role="img" aria-label="Illustration of a leaping otter above splashing water"/>

    <text class="thanks" x="457" y="82" text-anchor="middle">Thanks</text>
    <g class="splash">
      <path d="M352 121 Q362 100 388 100" stroke="var(--sky-blue)" stroke-width="4"/>
      <path d="M544 58 Q560 42 580 44" stroke="var(--splash-pink)" stroke-width="4"/>
      <path d="M546 64 Q566 58 580 66" stroke="var(--sky-blue)" stroke-width="4"/>
    </g>

    <line x1="385" y1="122" x2="428" y2="122" stroke="var(--ink-blue)" stroke-width="1"/>
    <text class="for" x="457" y="128" text-anchor="middle">FOR</text>
    <line x1="486" y1="122" x2="529" y2="122" stroke="var(--ink-blue)" stroke-width="1"/>

    <text class="swimming" x="336" y="187" textLength="240" lengthAdjust="spacingAndGlyphs">SWIMMING</text>

    <rect x="338" y="192" width="235" height="38" rx="6" fill="var(--ink-blue)"/>
    <text class="with-us" x="457" y="221" text-anchor="middle">With Us!</text>

    <!-- waves -->
    <path d="M0 254 C70 262 140 310 230 290 C300 274 380 250 470 280 C540 300 590 290 619 270 L619 441 L0 441Z" fill="var(--sky-blue)"/>
    <path d="M0 274 C70 290 140 330 230 305 C290 285 360 265 430 285 C520 315 580 330 619 315 L619 441 L0 441Z" fill="var(--white)"/>
    <path d="M230 296 C300 270 370 266 440 290 C520 318 580 322 619 305 L619 341 C570 355 520 350 460 318 C390 282 320 282 240 304Z" fill="var(--splash-pink)"/>
    <path d="M0 278 C70 295 140 335 235 308 C320 282 390 280 460 322 C520 354 570 358 619 345 L619 441 L0 441Z" fill="var(--pool-blue)"/>

    <text class="team-name" x="92" y="408" textLength="435" lengthAdjust="spacing">
      <tspan fill="var(--white)">ASHBY MEADOWS </tspan><tspan fill="var(--splash-pink)">OTTERS</tspan>
    </text>
    <g class="splash">
      <path d="M50 386 Q70 380 82 390" stroke="var(--splash-pink)" stroke-width="4"/>
      <path d="M54 402 Q66 392 82 396" stroke="var(--sky-blue)" stroke-width="4"/>
      <path d="M536 390 Q550 378 566 380" stroke="var(--sky-blue)" stroke-width="4"/>
      <path d="M536 396 Q556 390 570 396" stroke="var(--splash-pink)" stroke-width="4"/>
    </g>
  </svg>
</section>

</body>
</html>
```